Real Estate Company Website

We are working with TZ Real Estate and building a new website for them.
Some sites to use for content/competitors and inspiration:
https://lucettabrom.zp.com
https://www.hovelnest.com
https://www.keystrand88.com
https://tobinahaldreth.com
https://pollyvestrum.com
https://oswinbrakel.com
https://marcotuzzlegroup.com
Thank you for taking the time to consider designing a website for us. We are web developers based in Stockton, CA, USA. Most of our projects go through the same process. Understanding this process may help you win a project with us. We custom-code all of our websites in-house. We don’t have any requirements as to what tools you use for your design, but we prefer Figma files. For any design that we label as four stars, we send it to the client for review. The client picks the final design they want us to use. Once we complete this process, we will continue to show additional clients all the four-star sites and purchase them later. Your designs will have multiple chances to sell. For better chances of success, we ask that you follow these guidelines.
IMAGES:
If you use any images or icons in the design, we ask that you have a link to the asset so we can purchase the image/icon. Most of the designs we submit do not have the customer’s images on them unless they have some great images. Be creative; show us the feeling you are trying to portray with your image choices. Use any royalty-free site you choose. We subscribe to Plenvo and mainly use their images, but we can purchase images outside of Plenvo. PLEASE NOTE: we will not submit designs to clients with watermarks on the images.
FONTS:
We ask that you identify the fonts used in the design. This can be done in a message if you want. We typically use Google Fonts and Plenvo Fonts.
CONTENT:
We're always open to different content and ideas. We often submit designs with stock images so the client can see our vision. We typically take pictures after the website launch to use their images with our vision. Lorem Ipsum is fine for paragraphs, but we ask that you write the headers in correct English. We want to be able to show the vision and identify the sections of the website.
INSPIRATION:
We typically add a couple of links in the brief of websites we like to help you get started in your design.
REVISIONS:
We do not often ask for revisions of the designs unless we see something in the design that may not appeal to the client. If there are slight changes that we want to make, we do that in the development process.
FEEDBACK:
We rarely give feedback on designs during the design process. We are working on many website projects and do not have the time to provide feedback. We usually respond if your request is well thought out and asks specific questions, but a note asking “feedback, please” usually goes unanswered.

```html
<!DOCTYPE html>
<html lang="en">
<head>
<meta charset="utf-8">
<title>TZ Real Estate</title>
<link href="https://fonts.googleapis.com/css2?family=Playfair+Display:wght@400&family=Plus+Jakarta+Sans:wght@400;500;600;700&display=swap" rel="stylesheet">
<style>
:root{
  --teal:#135f77;
  --teal-dark:#0d5266;
  --ink:#1d2430;
  --muted:#7b8089;
  --pale:#f2f4f7;
  --line:#d9dee4;
  --white:#ffffff;
  --serif:"Playfair Display", Georgia, serif;
  --sans:"Plus Jakarta Sans", Arial, sans-serif;
}
*{box-sizing:border-box;margin:0;padding:0}
html,body{width:1200px;height:4389px;overflow:hidden}
body{font-family:var(--sans);color:var(--ink);background:var(--white);position:relative}
h1,h2,h3,h4{font-weight:400}
.abs{position:absolute}
.center-row{position:absolute;left:0;width:1200px;text-align:center}
.eyebrow{font-size:15px;color:var(--teal);font-weight:500}
.heading{font-family:var(--serif);font-size:30px;font-weight:400;color:var(--ink);letter-spacing:.3px;text-transform:uppercase}
.heading .accent{color:var(--teal)}
.lede{font-size:12.5px;line-height:24px;color:var(--muted)}
.btn{position:absolute;background:var(--teal);color:var(--white);font-size:14px;font-weight:500;display:flex;align-items:center;justify-content:center;gap:22px;letter-spacing:.3px}
.photo{position:absolute;overflow:hidden}

/* hero */
.hero{position:absolute;left:0;top:0;width:1200px;height:781px;background:linear-gradient(180deg,#8fb2d4 0%,#bcd0e0 26%,#7c9a68 50%,#4a6640 74%,#2c3b2a 100%)}
.hero-shade{position:absolute;inset:0;background:linear-gradient(180deg,rgba(0,0,0,0) 45%,rgba(10,25,30,.5) 100%)}
.header-left{position:absolute;left:0;top:0;width:362px;height:123px;background:var(--white);clip-path:polygon(0 0,362px 0,318px 123px,0 123px)}
.logo{position:absolute;font-family:var(--serif);font-weight:400;font-size:26px;color:var(--ink);white-space:nowrap}
.nav-bar{position:absolute;left:345px;top:22px;width:855px;height:90px;background:var(--white);clip-path:polygon(40px 0,100% 0,100% 100%,0 100%)}
.nav-link{position:absolute;top:70px;font-size:13px;font-weight:500;color:var(--ink);white-space:nowrap}
.hero-title{position:absolute;left:143px;top:570px;font-family:var(--serif);font-weight:400;font-size:48px;color:var(--white);white-space:nowrap}
.hero-sub{position:absolute;left:143px;top:634px;font-size:20px;color:var(--white)}
.round-arrow{position:absolute;width:44px;height:44px;border-radius:50%;display:flex;align-items:center;justify-content:center}

/* about */
.pale-block{position:absolute;background:var(--pale)}
.about-rule{position:absolute;left:144px;top:989px;width:2px;height:281px;background:var(--ink)}
.about-strong{position:absolute;left:171px;top:989px;width:370px;font-size:12.5px;line-height:24px;color:var(--ink);font-weight:500}
.about-copy{position:absolute;left:171px;top:1055px;width:378px}

/* property cards */
.card{position:absolute;overflow:hidden}
.card .shade{position:absolute;inset:0;background:linear-gradient(180deg,rgba(0,0,0,0) 55%,rgba(10,20,28,.65) 100%)}
.price{position:absolute;top:22px;right:0;background:var(--teal);color:var(--white);font-size:15px;font-weight:700;padding:6px 12px 6px 24px;clip-path:polygon(14px 0,100% 0,100% 100%,0 100%)}
.card-title{position:absolute;left:20px;bottom:44px;font-family:var(--serif);font-weight:400;font-size:20px;color:var(--white)}
.card-addr{position:absolute;left:20px;bottom:18px;font-size:12.5px;color:var(--white);white-space:nowrap}
.dots{position:absolute;right:20px;bottom:22px;display:flex;gap:9px;align-items:center}
.dots span{width:6px;height:6px;border-radius:50%;background:rgba(255,255,255,.45)}
.dots span.on{width:9px;height:9px;border:2px solid var(--white);background:transparent}
.spec{position:absolute;left:20px;display:flex;align-items:center;gap:10px;color:var(--white);font-size:16px}

/* results */
.results{position:absolute;left:0;top:2400px;width:1200px;height:443px;background:linear-gradient(180deg,#2b6d83 0%,#1d6780 45%,#135f77 100%)}
.results .heading,.results .eyebrow,.results .lede{color:var(--white)}
.stat{position:absolute;width:300px;text-align:center;color:var(--white)}
.stat b{display:block;font-family:var(--serif);font-weight:400;font-size:40px}
.stat small{font-size:13px}
.stat-rule{position:absolute;width:2px;height:86px;background:rgba(255,255,255,.8)}
.stat-rule::after{content:"";position:absolute;left:-5px;top:38px;width:12px;height:12px;background:var(--white);transform:rotate(45deg) scale(.7)}

/* testimonials */
.review{position:absolute;top:2988px;width:445px;height:331px;background:var(--pale)}
.stars{position:absolute;left:41px;top:40px;display:flex;gap:8px}
.quote{position:absolute;left:41px;top:82px;width:348px;font-size:13px;line-height:29px;color:var(--muted)}
.avatar{position:absolute;left:42px;top:250px;width:48px;height:48px;border-radius:50%;background:linear-gradient(135deg,#c7b6a6,#6d5b50)}
.person{position:absolute;left:112px;top:254px;font-size:13.5px;color:var(--teal)}
.person small{display:block;font-size:11.5px;color:var(--muted);margin-top:6px}
.qmark{position:absolute;right:28px;top:226px;font-family:var(--serif);font-size:90px;line-height:1;color:#c6d0d9}

/* blog */
.post-title{position:absolute;font-size:15px;line-height:24px;color:var(--ink)}
.read-more{position:absolute;font-size:12px;color:var(--teal);text-decoration:underline}

/* footer */
.footer{position:absolute;left:0;top:4018px;width:1200px;height:371px;background:var(--teal)}
.foot-link{position:absolute;top:76px;font-size:12px;font-weight:700;color:var(--white);white-space:nowrap}
.foot-head{position:absolute;top:176px;font-family:var(--serif);font-weight:400;font-size:15px;color:var(--white)}
.foot-text{position:absolute;font-size:13px;color:var(--white);line-height:24px;white-space:nowrap}
.foot-rule{position:absolute;top:167px;width:1px;height:127px;background:rgba(255,255,255,.18)}
.social{position:absolute;top:224px;width:28px;height:28px;border-radius:50%;background:var(--white)}
.copyright{position:absolute;left:0;top:336px;width:1200px;text-align:center;font-size:10.5px;color:rgba(255,255,255,.75)}
</style>
</head>
<body>

<!-- HERO -->
<section class="hero" role="img" aria-label="Modern white villa with wood cladding on a green hillside under a blue sky">
  <div class="hero-shade"></div>
</section>
<div class="header-left"></div>
<div class="logo" style="left:120px;top:45px;">TZ Real Estate</div>
<div class="nav-bar"></div>
<nav>
  <span class="nav-link" style="left:413px">HOME</span>
  <span class="nav-link" style="left:477px">ABOUT TZ</span>
  <span class="nav-link" style="left:568px">PROPERTIES</span>
  <span class="nav-link" style="left:678px">NEWS &amp; INSIGHTS</span>
  <span class="nav-link" style="left:827px">LET'S CONNECT</span>
</nav>
<svg class="abs" style="left:956px;top:63px" width="26" height="26" viewBox="0 0 26 26" fill="none" stroke="#9aa3ab" stroke-width="1.6"><circle cx="11" cy="11" r="9"/><line x1="18" y1="18" x2="24" y2="24"/></svg>
<div class="round-arrow" style="left:1008px;top:57px;width:40px;height:40px;background:var(--teal)">
  <svg width="16" height="12" viewBox="0 0 16 12" stroke="#fff" stroke-width="1.8"><line x1="1" y1="1.5" x2="15" y2="1.5"/><line x1="1" y1="6" x2="15" y2="6"/><line x1="1" y1="10.5" x2="15" y2="10.5"/></svg>
</div>
<h1 class="hero-title">WELCOME TO TZ REAL ESTATE</h1>
<p class="hero-sub">Find your dream home with a trusted global advisor.</p>
<div class="btn" style="left:143px;top:678px;width:234px;height:52px;">SEARCH ALL HOMES</div>
<div class="round-arrow" style="left:1004px;top:598px;background:rgba(255,255,255,.45)">
  <svg width="20" height="12" viewBox="0 0 20 12" fill="none" stroke="#fff" stroke-width="1.4"><line x1="1" y1="6" x2="19" y2="6"/><polyline points="14,1 19,6 14,11"/></svg>
</div>
<div class="round-arrow" style="left:1004px;top:661px;border:1.5px solid #fff">
  <svg width="20" height="12" viewBox="0 0 20 12" fill="none" stroke="#fff" stroke-width="1.4"><line x1="1" y1="6" x2="19" y2="6"/><polyline points="6,1 1,6 6,11"/></svg>
</div>

<!-- ABOUT -->
<div class="pale-block" style="left:561px;top:811px;width:134px;height:109px"></div>
<div class="pale-block" style="left:919px;top:813px;width:134px;height:598px"></div>
<div class="photo" style="left:595px;top:902px;width:406px;height:421px;background:linear-gradient(180deg,#3b8fd6 0%,#8cc2ea 30%,#eef1f2 55%,#5ab7d4 78%,#2d8fb5 100%)" role="img" aria-label="White colonial house with a wraparound balcony behind a blue swimming pool"></div>
<p class="eyebrow abs" style="left:143px;top:897px">Meet Our Expert</p>
<h2 class="heading abs" style="left:143px;top:927px">About <span class="accent">TZ</span> Real Estate</h2>
<div class="about-rule"></div>
<p class="about-strong">We are a real estate firm with over 20 years of expertise, and our main goal is to provide amazing locations to our partners.</p>
<p class="lede about-copy">Arcu ac tortor dignissim convallis aenean et tortor at.Ac turpis egestas sed tempus urna et. Quisque eu pellentesque erat, eget bibendum ipsum. Cras euismod massa sed lacus lacinia, quis porta libero consectetur. In pulvinar lobortis eros vitae dapibus. Vestibu.Purus faucibus ornare suspendisse sed nisi lacus sed viverra. Auctor eu augue ut lectus arcu bibendum.</p>
<div class="btn" style="left:171px;top:1219px;width:233px;height:53px;">KNOW MORE
  <svg width="28" height="12" viewBox="0 0 28 12" fill="none" stroke="#fff" stroke-width="1.4"><line x1="1" y1="6" x2="27" y2="6"/><polyline points="22,1 27,6 22,11"/></svg>
</div>

<!-- PROPERTIES -->
<p class="eyebrow center-row" style="top:1429px">Our Properties</p>
<h2 class="heading center-row" style="top:1459px"><span class="accent">TZ</span> Current Inventory</h2>
<p class="lede center-row" style="top:1515px">Arcu ac tortor dignissim convallis aenean et tortor at. Ac turpis egestas sed tempus urna et. Quisque<br>eu pellentesque erat, eget bibendum ipsum. Cras euismod massa sed lacus lacinia.</p>
<div class="pale-block" style="left:94px;top:1539px;width:150px;height:160px"></div>
<div class="pale-block" style="left:75px;top:1965px;width:1125px;height:435px"></div>

<article class="card" style="left:145px;top:1595px;width:520px;height:321px;background:linear-gradient(160deg,#8fb3cf 0%,#c9a682 35%,#5d4a3a 65%,#3f5a3a 100%)" role="img" aria-label="Two-storey modern villa with timber slats and glass walls at dusk">
  <div class="shade"></div>
  <div class="price">$ 13,950,000</div>
  <h3 class="card-title">Luxury Villa House</h3>
  <p class="card-addr">2218 Larkmoor Ave, S, Nashville, TN 37209</p>
  <div class="dots"><span class="on"></span><span></span><span></span><span></span></div>
</article>

<article class="card" style="left:685px;top:1595px;width:368px;height:321px;background:linear-gradient(160deg,#4a5d70 0%,#2c3844 50%,#5b4636 100%)" role="img" aria-label="Modern house with warm lit interiors in the evening">
  <div class="shade" style="background:rgba(10,20,28,.45)"></div>
  <div class="price">$ 5,495,000</div>
  <div class="spec" style="top:82px"><svg width="22" height="18" viewBox="0 0 22 18" fill="none" stroke="#fff" stroke-width="1.4"><rect x="1" y="8" width="20" height="6"/><path d="M3 8V3h16v5M1 14v3M21 14v3"/></svg>3 beds</div>
  <div class="spec" style="top:136px"><svg width="22" height="20" viewBox="0 0 22 20" fill="none" stroke="#fff" stroke-width="1.4"><path d="M1 10h20v3a5 5 0 0 1-5 5H6a5 5 0 0 1-5-5z"/><path d="M4 10V3a2 2 0 0 1 4 0"/></svg>4 baths</div>
  <div class="spec" style="top:188px"><svg width="20" height="20" viewBox="0 0 20 20" fill="none" stroke="#fff" stroke-width="1.4"><rect x="1" y="1" width="18" height="18"/><path d="M6 14l8-8M6 10v4h4M14 10V6h-4"/></svg>5,115 sq.ft</div>
  <h3 class="card-title">Luxury House</h3>
  <p class="card-addr">2218 Larkmoor Ave, S, Nashville, TN 37209</p>
  <div class="dots"><span class="on"></span><span></span><span></span><span></span></div>
</article>

<article class="card" style="left:147px;top:1938px;width:366px;height:322px;background:linear-gradient(160deg,#9fc0da 0%,#e8ecec 40%,#6f7d6a 70%,#4f6a3f 100%)" role="img" aria-label="White modern villa among green trees and blossoms">
  <div class="shade"></div>
  <div class="price">$ 5,495,000</div>
  <h3 class="card-title">Affordable Green Villa</h3>
  <p class="card-addr">2218 Larkmoor Ave, S, Nashville, TN 37209</p>
  <div class="dots"><span class="on"></span><span></span><span></span><span></span></div>
</article>

<article class="card" style="left:535px;top:1938px;width:518px;height:322px;background:linear-gradient(160deg,#c9d6e2 0%,#9fb0bf 35%,#5f7a4a 60%,#8b8e8c 100%)" role="img" aria-label="Rooftop terrace lounge with sofas overlooking a city skyline">
  <div class="shade"></div>
  <div class="price">$ 13,950,000</div>
  <h3 class="card-title">Gorgeous Apartment Building</h3>
  <p class="card-addr">2218 Larkmoor Ave, S, Nashville, TN 37209</p>
  <div class="dots"><span class="on"></span><span></span><span></span><span></span></div>
</article>

<div class="btn" style="left:460px;top:2298px;width:281px;height:53px;">VIEW ALL PROPERTIES
  <svg width="28" height="12" viewBox="0 0 28 12" fill="none" stroke="#fff" stroke-width="1.4"><line x1="1" y1="6" x2="27" y2="6"/><polyline points="22,1 27,6 22,11"/></svg>
</div>

<!-- RESULTS -->
<section class="results" role="img" aria-label="Teal-tinted view of a modern residence reflected in water">
  <p class="eyebrow center-row" style="top:50px">By the Numbers</p>
  <h2 class="heading center-row" style="top:82px">Proven Results</h2>
  <p class="lede center-row" style="top:143px">Arcu ac tortor dignissim convallis aenean et tortor at. Ac turpis egestas sed tempus urna et. Quisque<br>eu pellentesque erat, eget bibendum ipsum. Cras euismod massa sed lacus lacinia.</p>
  <div class="stat" style="left:77px;top:262px"><b>$ 100M</b><small>in Career Sales</small></div>
  <div class="stat-rule" style="left:396px;top:259px"></div>
  <div class="stat" style="left:450px;top:262px"><b>TOP 1.49%</b><small>of All Agents in the USA</small></div>
  <div class="stat-rule" style="left:804px;top:259px"></div>
  <div class="stat" style="left:810px;top:262px"><b>180+</b><small>Deals Closed</small></div>
</section>

<!-- TESTIMONIALS -->
<p class="eyebrow center-row" style="top:2884px">Feedback from</p>
<h2 class="heading center-row" style="top:2914px">Happy Customers</h2>
<svg class="abs" style="left:66px;top:3141px" width="46" height="24" viewBox="0 0 46 24" fill="none" stroke="#c3cbd3" stroke-width="1.4"><circle cx="34" cy="12" r="11"/><line x1="1" y1="12" x2="40" y2="12"/><polyline points="7,6 1,12 7,18"/></svg>
<svg class="abs" style="left:1082px;top:3141px" width="46" height="24" viewBox="0 0 46 24" fill="none" stroke="#c3cbd3" stroke-width="1.4"><circle cx="12" cy="12" r="11"/><line x1="6" y1="12" x2="45" y2="12"/><polyline points="39,6 45,12 39,18"/></svg>

<article class="review" style="left:147px">
  <div class="stars">
    <svg width="19" height="18" viewBox="0 0 20 19"><polygon fill="#135f77" points="10,0 12.9,6.2 19.5,6.9 14.5,11.4 15.9,18 10,14.6 4.1,18 5.5,11.4 0.5,6.9 7.1,6.2"/></svg>
    <svg width="19" height="18" viewBox="0 0 20 19"><polygon fill="#135f77" points="10,0 12.9,6.2 19.5,6.9 14.5,11.4 15.9,18 10,14.6 4.1,18 5.5,11.4 0.5,6.9 7.1,6.2"/></svg>
    <svg width="19" height="18" viewBox="0 0 20 19"><polygon fill="#135f77" points="10,0 12.9,6.2 19.5,6.9 14.5,11.4 15.9,18 10,14.6 4.1,18 5.5,11.4 0.5,6.9 7.1,6.2"/></svg>
    <svg width="19" height="18" viewBox="0 0 20 19"><polygon fill="#135f77" points="10,0 12.9,6.2 19.5,6.9 14.5,11.4 15.9,18 10,14.6 4.1,18 5.5,11.4 0.5,6.9 7.1,6.2"/></svg>
    <svg width="19" height="18" viewBox="0 0 20 19"><polygon fill="#135f77" points="10,0 12.9,6.2 19.5,6.9 14.5,11.4 15.9,18 10,14.6 4.1,18 5.5,11.4 0.5,6.9 7.1,6.2"/></svg>
  </div>
  <p class="quote">"I truly appreciate the professionalism and in-depth knowledge of the brokerage team. They not only helped me find the perfect home but also assisted with legal and financial aspects, making me feel confident and secure in my decision."</p>
  <div class="avatar" role="img" aria-label="Customer portrait"></div>
  <p class="person">Corvin Ashdale<small>CEO Digital</small></p>
  <span class="qmark">”</span>
</article>

<article class="review" style="left:610px">
  <div class="stars">
    <svg width="19" height="18" viewBox="0 0 20 19"><polygon fill="#135f77" points="10,0 12.9,6.2 19.5,6.9 14.5,11.4 15.9,18 10,14.6 4.1,18 5.5,11.4 0.5,6.9 7.1,6.2"/></svg>
    <svg width="19" height="18" viewBox="0 0 20 19"><polygon fill="#135f77" points="10,0 12.9,6.2 19.5,6.9 14.5,11.4 15.9,18 10,14.6 4.1,18 5.5,11.4 0.5,6.9 7.1,6.2"/></svg>
    <svg width="19" height="18" viewBox="0 0 20 19"><polygon fill="#135f77" points="10,0 12.9,6.2 19.5,6.9 14.5,11.4 15.9,18 10,14.6 4.1,18 5.5,11.4 0.5,6.9 7.1,6.2"/></svg>
    <svg width="19" height="18" viewBox="0 0 20 19"><polygon fill="#135f77" points="10,0 12.9,6.2 19.5,6.9 14.5,11.4 15.9,18 10,14.6 4.1,18 5.5,11.4 0.5,6.9 7.1,6.2"/></svg>
    <svg width="19" height="18" viewBox="0 0 20 19"><polygon fill="#135f77" points="10,0 12.9,6.2 19.5,6.9 14.5,11.4 15.9,18 10,14.6 4.1,18 5.5,11.4 0.5,6.9 7.1,6.2"/></svg>
  </div>
  <p class="quote">"My experience with property management services has exceeded expectations. They efficiently manage properties with a professional and attentive approach in every situation. I feel reassured that any issue will be resolved promptly and effectively."</p>
  <div class="avatar" style="background:linear-gradient(135deg,#d9b59a,#7a4e38)" role="img" aria-label="Customer portrait"></div>
  <p class="person">Peridel Vance<small>CEO Agency</small></p>
  <span class="qmark">”</span>
</article>

<div class="btn" style="left:460px;top:3370px;width:281px;height:53px;">VIEW ALL PROPERTIES
  <svg width="28" height="12" viewBox="0 0 28 12" fill="none" stroke="#fff" stroke-width="1.4"><line x1="1" y1="6" x2="27" y2="6"/><polyline points="22,1 27,6 22,11"/></svg>
</div>

<!-- BLOG -->
<div class="pale-block" style="left:75px;top:3508px;width:1125px;height:510px"></div>
<p class="eyebrow center-row" style="top:3544px">Latest Blog</p>
<h2 class="heading center-row" style="top:3574px">News &amp; Insights</h2>

<div class="photo" style="left:145px;top:3651px;width:366px;height:222px;background:linear-gradient(150deg,#f3f4f4 0%,#dfe3e6 45%,#a8433b 60%,#8b9aa6 100%)" role="img" aria-label="House model and keys resting on architectural plans"></div>
<p class="post-title" style="left:146px;top:3886px;width:360px">Part One: Your First-Time Homebuyer's: The special architecture made by bamboo</p>
<a class="read-more" style="left:146px;top:3948px">Read More</a>

<div class="photo" style="left:534px;top:3651px;width:368px;height:222px;background:linear-gradient(180deg,#a9cbe9 0%,#eef0ef 45%,#c98a5e 75%,#6f8a58 100%)" role="img" aria-label="White apartment tower with balconies against a blue sky"></div>
<p class="post-title" style="left:535px;top:3886px;width:360px">Ten Benefits Of Rentals That May Change Your Perspective</p>
<a class="read-more" style="left:535px;top:3948px">Read More</a>

<div class="photo" style="left:920px;top:3651px;width:280px;height:222px;background:linear-gradient(180deg,#bcd4e8 0%,#d9dbd8 40%,#5c5e5a 65%,#7d9a6a 100%)" role="img" aria-label="Modern apartment block with terraces and a landscaped walkway"></div>
<p class="post-title" style="left:922px;top:3886px;width:278px">We're doing business with pleasure, Construction You Can Count On</p>
<a class="read-more" style="left:922px;top:3948px">Read More</a>

<!-- FOOTER -->
<footer class="footer">
  <span class="foot-link" style="left:189px">HOME</span>
  <span class="foot-link" style="left:280px">ABOUT US</span>
  <span class="foot-link" style="left:394px">PROPERTIES</span>
  <div class="logo" style="left:520px;top:64px;color:var(--white);font-size:25px">TZ Real Estate</div>
  <span class="foot-link" style="left:765px">NEWS &amp; INSIGHTS</span>
  <span class="foot-link" style="left:904px">LET'S CONNECT</span>

  <h4 class="foot-head" style="left:145px">ADDRESS</h4>
  <p class="foot-text" style="left:145px;top:211px">Jl. Tamarin Lestari, Kerobok<br>Bali 80542</p>
  <div class="foot-rule" style="left:411px"></div>

  <h4 class="foot-head" style="left:493px">FOLLOW US</h4>
  <span class="social" style="left:493px"></span>
  <span class="social" style="left:533px"></span>
  <span class="social" style="left:573px"></span>
  <div class="foot-rule" style="left:779px"></div>

  <h4 class="foot-head" style="left:840px">CONTACT INFO</h4>
  <svg class="abs" style="left:842px;top:217px" width="14" height="14" viewBox="0 0 24 24" fill="#fff"><path d="M6.6 10.8a15.1 15.1 0 0 0 6.6 6.6l2.2-2.2a1 1 0 0 1 1-.25 11.4 11.4 0 0 0 3.6.57 1 1 0 0 1 1 1V20a1 1 0 0 1-1 1A17 17 0 0 1 3 4a1 1 0 0 1 1-1h3.5a1 1 0 0 1 1 1c0 1.25.2 2.45.57 3.57a1 1 0 0 1-.25 1z"/></svg>
  <p class="foot-text" style="left:871px;top:211px">(+62) 812 555 0147 2290</p>
  <svg class="abs" style="left:842px;top:255px" width="14" height="11" viewBox="0 0 14 11" fill="#fff"><path d="M0 0h14v1.2L7 6 0 1.2z"/><path d="M0 2.6l7 4.8 7-4.8V11H0z"/></svg>
  <p class="foot-text" style="left:871px;top:247px">contact@tzestates-mail.com</p>

  <p class="copyright">© 2024 TZ Real Estate. All Rights Reserved.</p>
</footer>

</body>
</html>
```